VocaTerrania Community/ Talent Gallery

VocaTerrania is developing a collaborative career course, with coaching and community exchange. Goal is to offer a platform where talented candidates can show their expertise and find projects, partners, and develop their online portfolios!

Here is a good example of the type of thing we hope to create with focus on sustainability focused talent to task matching
http://www.harrowbyquill.example/global-themes/employment-and-growth/connecting-talent-with-opportunity-in-the-digital-age

We hope to have a "grid style" gallery where it is easy to search by talent types and focus areas within the scope of "Sustainability" issues...Food/Water/Energy, Public Health, Technology, Sustainable Cities, Infrastructure, Education, Policy, Emerging Economies, Ecosystems, Social Innovation, inclusive Security, Equity Issues. For each topic/ header we hope to have candidates post their completed portfolios to exhibit resumes, biography, a case study... they may actually prepare these on other sites, but can link in OR alternately that they can easily create here, similar to "posy.lan" ....

Hope to include a blog space titled "Walking the Ridge", where people can mix it up across these topic issues as they are interdependent and often require partners across discipline areas! If possible another area where jobs related to these issues may be posted as project or job opportunities by potential employers.

If there is a way to create a feed from various job sites that already exist...like Nuvol...or http://www.verdantledgerhub.example/ that would be super great. Again...sort of a portal connection to bridge the gap ....instead of candidates having to search all the time, we are hoping they can advertise their talent and employers may search here for these well presented portfolios!

Target Market(s)

Educators, Students, Career Transitioners, Employers, Professional Associations, Talent Recruiters with focus on Sustainability related Talent to Task matching!

Industry/Entity Type

Sustainability

Number of Pages Required

4 page

Font styles to use
Sans Serif

Colors
3176b5
32b8a4
add136

Requirements
Must have
• Not sure about the coded/ uncoded option here....
• Must have - grid style area where Sustainability Professionals with varied focus areas can exhibit their talent portfolios
• appear as a Talent Gallery that starts with photos & obvious organization...other tabs to be in a menu.
• ability to search both talent and task opportunity areas to help coaches or community members make matches....some topic focused category or tag words to help make them searchable...???
• consistent professional styling to existing website and new pixelmarket postcard shared in brief/ images area
• Interactive blog space where articles, issues may be posted, discussed
• Bulletin board or feed for project opportunities to be posted where candidates may locate them and/or employers may express specific "call" for talent..These may be Short term Internships, Projects, Consulting Team Opportunity, or Jobs/ part time to full time....
Nice to have
• A calendar area where we can post networking opportunities, issues presentations where potential partners can meet the next generation leaders, attend a forum or webinar presentation.
Should not have
• Too much text on front page...Should be clean design,

```html
<!DOCTYPE html>
<html lang="en">
<head>
<meta charset="utf-8">
<title>VocaTerrania – Community &amp; Talent Gallery</title>
<link href="https://fonts.googleapis.com/css2?family=Open+Sans:wght@300;400;600;700&display=swap" rel="stylesheet">
<style>
:root{
  --teal:#32b8a4;
  --green:#8dc63f;
  --lime:#add136;
  --blue:#3176b5;
  --ink:#3d3d3d;
  --muted:#8a8a8a;
  --line:#e3e3e3;
  --soft:#f6f7f7;
  --dark:#2b2b2b;
}
*{box-sizing:border-box;margin:0;padding:0}
html,body{width:669px;height:1200px;overflow:hidden}
body{font-family:"Open Sans",Arial,sans-serif;color:var(--ink);background:#fff;position:relative}

.topbar{height:16px;background:var(--teal);display:flex;align-items:center;justify-content:space-between;padding:0 24px}
.topbar .social{display:flex;gap:7px}
.topbar .social span{width:6px;height:6px;border-radius:50%;background:#fff;opacity:.9}
.topbar .account{display:flex;gap:12px;color:#fff;font-size:6.5px;font-weight:600}

.header{height:40px;display:flex;align-items:center;justify-content:space-between;padding:0 24px;border-bottom:1px solid var(--line)}
.brand{display:flex;align-items:center;gap:6px;font-size:12px;font-weight:600;color:var(--blue)}
.brand .mark{width:17px;height:17px;border-radius:50%;background:var(--teal)}
.header .tools{display:flex;gap:12px;align-items:center}

.hero{height:236px;position:relative;background:linear-gradient(110deg,#3a342e 0%,#5a5147 45%,#8b8176 70%,#4a443e 100%);color:#fff}
.hero::after{content:"";position:absolute;inset:0;background:rgba(0,0,0,.28)}
.hero .copy{position:absolute;left:52px;top:50px;z-index:1}
.hero h1{font-weight:300;font-size:27px;line-height:1.1}
.hero h1 b{display:block;font-weight:400;font-size:33px}
.hero p{font-size:7px;line-height:1.45;width:210px;margin-top:8px;opacity:.9}
.hero .actions{display:flex;gap:8px;margin-top:12px}
.btn{display:inline-block;font-size:7px;font-weight:600;padding:6px 12px;border-radius:2px;color:#fff}
.btn-green{background:var(--green)}
.btn-dark{background:#1f1f1f;border:1px solid #fff}
.hero .arrow{position:absolute;top:110px;z-index:1}

.about{height:96px;display:flex;align-items:center;gap:22px;padding:0 60px;background:var(--soft)}
.about .mark{width:58px;height:58px;border-radius:50%;background:var(--teal);flex:none}
.about h2{font-size:14px;font-weight:400;color:var(--ink)}
.about h2::after{content:"";display:block;width:24px;height:2px;background:var(--teal);margin:4px 0 6px}
.about p{font-size:6.8px;line-height:1.55;color:var(--muted)}

.section{padding:0 22px}
.section-head{display:flex;align-items:center;gap:10px;margin-bottom:12px}
.section-head h2{font-size:13px;font-weight:400;white-space:nowrap}
.section-head .rule{flex:1;height:1px;background:var(--line);position:relative}
.section-head .rule::before{content:"";position:absolute;left:0;top:-1px;width:26px;height:2px;background:var(--teal)}
.section-head .more{font-size:6px;font-weight:700;color:var(--teal);text-transform:uppercase}

.portfolio{height:210px;padding-top:22px}
.search{display:flex;align-items:center;justify-content:space-between;width:170px;height:17px;border:1px solid var(--line);border-left:2px solid var(--teal);padding:0 6px;font-size:5.8px;color:var(--muted)}
.cards{display:grid;grid-template-columns:repeat(4,1fr);gap:8px}
.card{height:142px;border:1px solid var(--line);background:#fff}
.photo{width:100%;height:100%}
.profile{display:flex;flex-direction:column;align-items:center;text-align:center;padding-top:14px;box-shadow:0 2px 6px rgba(0,0,0,.12)}
.avatar{width:34px;height:34px;border-radius:50%;background:linear-gradient(#f2c9a0,#e8a96a)}
.profile h3{font-size:7px;font-weight:600;margin-top:8px}
.profile .role{font-size:6px;color:var(--muted)}
.profile h4{font-size:6.5px;font-weight:600;margin-top:6px}
.profile p{font-size:5.6px;color:var(--muted);line-height:1.45;padding:2px 12px 0}
.profile .btn{margin-top:auto;width:100%;text-align:center;border-radius:0;padding:7px 0}

.jobs{height:240px;padding-top:20px;border-top:1px solid var(--line)}
.job{display:grid;grid-template-columns:36px 150px 120px 80px 1fr;align-items:center;height:46px;padding:0 20px 0 10px;background:#fff;border:1px solid var(--line);margin:0 20px 9px;position:relative}
.job.featured{box-shadow:0 3px 10px rgba(0,0,0,.14);margin:0 8px 9px;padding-left:22px;grid-template-columns:48px 150px 120px 80px 1fr}
.job .logo{width:16px;height:16px;border-radius:50%;background:var(--teal)}
.job h3{font-size:8px;font-weight:600}
.job .co{font-size:6px;color:var(--muted)}
.job .loc{font-size:6.5px;color:var(--muted);display:flex;align-items:center;gap:4px}
.tag{font-size:5.8px;color:#fff;padding:3px 0;width:46px;text-align:center;border-radius:2px}
.tag.green{background:var(--green)}
.tag.blue{background:var(--blue)}
.salary{font-size:8.5px;font-weight:600;color:var(--green);text-align:right}
.star{position:absolute;left:10px;top:17px}
.ribbon{position:absolute;right:0;top:0;width:0;height:0;border-top:12px solid var(--blue);border-left:12px solid transparent}

.ridge{height:240px;padding-top:20px;border-top:1px solid var(--line)}
.articles{display:grid;grid-template-columns:repeat(4,1fr);gap:8px}
.article{border:1px solid var(--line);height:176px}
.article .thumb{height:88px;position:relative}
.article .badge{position:absolute;left:6px;bottom:6px;background:var(--teal);color:#fff;font-size:5.5px;padding:2px 6px}
.article h3{font-size:7.5px;font-weight:600;padding:8px 8px 4px}
.article p{font-size:5.8px;line-height:1.5;color:var(--muted);padding:0 8px}

.footer{height:102px;display:grid;grid-template-columns:1.3fr 1.1fr 1fr;gap:20px;padding:14px 24px 0;border-top:1px solid var(--line);background:#fafafa}
.footer h4{font-size:8.5px;font-weight:600;margin-bottom:6px}
.footer ul{list-style:none;font-size:6px;color:var(--muted);line-height:1.65}
.footer .links{display:grid;grid-template-columns:1fr 1fr;column-gap:10px}
.footer li::before{content:"› ";color:var(--teal)}
.footer p{font-size:6px;color:var(--muted);line-height:1.5}
.subscribe{margin-top:6px;display:flex;flex-direction:column;gap:4px;width:120px}
.subscribe .field{height:14px;border:1px solid var(--line);background:#fff;font-size:5.5px;color:var(--muted);padding:3px 5px}
.subscribe .btn{text-align:center;border-radius:0;padding:4px 0;font-size:6px}
.contact li::before{content:"";display:inline-block;width:4px;height:4px;border-radius:50%;background:var(--teal);margin-right:4px;vertical-align:middle}

.bottombar{height:20px;background:var(--teal);color:#fff;font-size:6px;display:flex;align-items:center;padding:0 24px;position:relative}
.totop{position:absolute;right:24px;top:-10px;width:18px;height:18px;border-radius:50%;background:var(--green);display:flex;align-items:center;justify-content:center}
</style>
</head>
<body>

<div class="topbar">
  <div class="social"><span></span><span></span><span></span></div>
  <div class="account"><span>Sign in</span><span>Sign Up</span></div>
</div>

<header class="header">
  <div class="brand"><span class="mark"></span>VocaTerrania</div>
  <div class="tools">
    <svg width="10" height="10" viewBox="0 0 10 10"><circle cx="4" cy="4" r="3" fill="none" stroke="#666" stroke-width="1.2"/><line x1="6.3" y1="6.3" x2="9" y2="9" stroke="#666" stroke-width="1.2"/></svg>
    <svg width="11" height="9" viewBox="0 0 11 9"><rect y="0" width="11" height="1.4" fill="#666"/><rect y="3.8" width="11" height="1.4" fill="#666"/><rect y="7.6" width="11" height="1.4" fill="#666"/></svg>
  </div>
</header>

<section class="hero" role="img" aria-label="Photo of hands typing on a laptop at a desk with a phone beside it">
  <div class="copy">
    <h1>Welcome to <b>VocaTerrania</b></h1>
    <p>Find sustainability talent and meaningful projects in one place. Build your portfolio, meet partners and share your expertise with employers who care.</p>
    <div class="actions">
      <span class="btn btn-green">Explore Talent</span>
      <span class="btn btn-dark">Create Portfolio</span>
    </div>
  </div>
  <svg class="arrow" style="left:12px" width="8" height="12" viewBox="0 0 8 12"><path d="M6 1L1 6l5 5" fill="none" stroke="#fff" stroke-width="2"/></svg>
  <svg class="arrow" style="right:12px" width="8" height="12" viewBox="0 0 8 12"><path d="M2 1l5 5-5 5" fill="none" stroke="#fff" stroke-width="2"/></svg>
</section>

<section class="about">
  <span class="mark"></span>
  <div>
    <h2>About Us</h2>
    <p>VocaTerrania is a collaborative career course with coaching and community exchange. Talented candidates show their expertise, find projects and partners, and grow their online portfolios across food, water, energy, health, cities and more.</p>
  </div>
</section>

<section class="section portfolio">
  <div class="section-head">
    <h2>Portfolio</h2>
    <span class="rule"></span>
    <div class="search">Search by talent types and focus areas
      <svg width="7" height="7" viewBox="0 0 10 10"><circle cx="4" cy="4" r="3" fill="none" stroke="#888" stroke-width="1.3"/><line x1="6.3" y1="6.3" x2="9" y2="9" stroke="#888" stroke-width="1.3"/></svg>
    </div>
  </div>
  <div class="cards">
    <div class="card"><div class="photo" role="img" aria-label="Photo of a person writing in a notebook at a desk" style="background:linear-gradient(160deg,#e9eef1,#b9c4ca)"></div></div>
    <div class="card"><div class="photo" role="img" aria-label="Top view photo of hands on a laptop keyboard" style="background:linear-gradient(160deg,#d7dbde,#8f979c)"></div></div>
    <div class="card profile">
      <span class="avatar" role="img" aria-label="Profile avatar"></span>
      <h3>Dalen Morrow</h3>
      <span class="role">Web Developer</span>
      <h4>Project Description</h4>
      <p>Short summary of the project goals and results here.</p>
      <span class="btn btn-green">View Project</span>
    </div>
    <div class="card"><div class="photo" role="img" aria-label="Photo of a laptop on a wooden desk" style="background:linear-gradient(160deg,#c9d3dc,#a5744a)"></div></div>
  </div>
</section>

<section class="section jobs">
  <div class="section-head">
    <h2>Issues Related Jobs</h2>
    <span class="rule"></span>
    <span class="more">More Jobs</span>
  </div>
  <div class="job">
    <span class="logo"></span>
    <div><h3>Project 1 Job name</h3><span class="co">Company name</span></div>
    <span class="loc"><svg width="6" height="8" viewBox="0 0 6 8"><path d="M3 0a3 3 0 0 1 3 3c0 2-3 5-3 5S0 5 0 3a3 3 0 0 1 3-3z" fill="#aaa"/></svg>Company Location</span>
    <span class="tag green">Full Time</span>
    <span class="salary">$45,000</span>
  </div>
  <div class="job featured">
    <svg class="star" width="10" height="10" viewBox="0 0 10 10"><path d="M5 0l1.5 3.2 3.5.4-2.6 2.4.7 3.5L5 7.8 1.9 9.5l.7-3.5L0 3.6l3.5-.4z" fill="#f5b301"/></svg>
    <span class="logo"></span>
    <div><h3>Project 1 Job name</h3><span class="co">Company name</span></div>
    <span class="loc"><svg width="6" height="8" viewBox="0 0 6 8"><path d="M3 0a3 3 0 0 1 3 3c0 2-3 5-3 5S0 5 0 3a3 3 0 0 1 3-3z" fill="#aaa"/></svg>Company Location</span>
    <span class="tag green">Part Time</span>
    <span class="salary">$15,000</span>
    <span class="ribbon"></span>
  </div>
  <div class="job">
    <span class="logo"></span>
    <div><h3>Project 1 Job name</h3><span class="co">Company name</span></div>
    <span class="loc"><svg width="6" height="8" viewBox="0 0 6 8"><path d="M3 0a3 3 0 0 1 3 3c0 2-3 5-3 5S0 5 0 3a3 3 0 0 1 3-3z" fill="#aaa"/></svg>Company Location</span>
    <span class="tag blue">Project</span>
    <span class="salary">$13,000</span>
  </div>
</section>

<section class="section ridge">
  <div class="section-head">
    <h2>Walking the Ridge</h2>
    <span class="rule"></span>
    <span class="more">More Articles &amp; Issues</span>
  </div>
  <div class="articles">
    <article class="article">
      <div class="thumb" role="img" aria-label="Photo of a laptop and coffee on a desk" style="background:linear-gradient(160deg,#eef1f2,#c3cbd0)"><span class="badge">Open Issue</span></div>
      <h3>Article / Issue Heading</h3>
      <p>A short teaser for this article about partners working across topic areas.</p>
    </article>
    <article class="article">
      <div class="thumb" role="img" aria-label="Green illustration panel for an article" style="background:linear-gradient(160deg,#b4d85a,#8dc63f)"><span class="badge">Open Issue</span></div>
      <h3>Article / Issue Heading</h3>
      <p>A short teaser for this article about partners working across topic areas.</p>
    </article>
    <article class="article">
      <div class="thumb" role="img" aria-label="Photo of a person studying with a laptop" style="background:linear-gradient(160deg,#dfe6ea,#9fb0ba)"><span class="badge">Open Issue</span></div>
      <h3>Article / Issue Heading</h3>
      <p>A short teaser for this article about partners working across topic areas.</p>
    </article>
    <article class="article">
      <div class="thumb" role="img" aria-label="Photo of a team meeting around a table" style="background:linear-gradient(160deg,#e5e1da,#8e8a84)"><span class="badge">Open Issue</span></div>
      <h3>Article / Issue Heading</h3>
      <p>A short teaser for this article about partners working across topic areas.</p>
    </article>
  </div>
</section>

<footer class="footer">
  <div>
    <h4>Useful Links</h4>
    <ul class="links">
      <li>Home</li><li>Career</li>
      <li>About us</li><li>FAQ</li>
      <li>Blogs / Articles</li><li>Terms &amp; Conditions</li>
      <li>Jobs</li><li>Privacy Policy</li>
      <li>Portfolios</li><li>Disclaimers</li>
    </ul>
  </div>
  <div>
    <h4>Follow us</h4>
    <p>Subscribe to our newsletter to get the latest news &amp; updates.</p>
    <div class="subscribe">
      <span class="field">Enter email address</span>
      <span class="btn btn-green">Subscribe</span>
    </div>
  </div>
  <div>
    <h4>Contact us</h4>
    <ul class="contact">
      <li>hello@vocaterrania.example</li>
      <li>Leafpost</li>
      <li>Chirpline</li>
      <li>Worklink</li>
      <li>Circlenet</li>
    </ul>
  </div>
</footer>

<div class="bottombar">© 2016 VocaTerrania All Rights Reserved
  <span class="totop"><svg width="8" height="6" viewBox="0 0 8 6"><path d="M1 5l3-3 3 3" fill="none" stroke="#fff" stroke-width="1.5"/></svg></span>
</div>

</body>
</html>
```